Brenton Wealth Management Flow Charts

I need help creating three flow charts for my businesses website. We want them to be simple but look professional. This is for a Wealth Management firm. I will attach a word document that has all of the descriptions for everything so you know what icons to use. We just want the chart to have an icon, the names of each step and the corresponding numbers. I will also include some examples of charts we liked as well. Once the winner is selected, we will need help with additional graphic design elements for our website ASAP.
- Goudy Roman

```html
<!DOCTYPE html>
<html lang="en">
<head>
<meta charset="utf-8">
<title>Brenton Wealth Management – Flow Charts</title>
<link rel="stylesheet" href="https://fonts.googleapis.com/css2?family=Montserrat:wght@500;700;800&display=swap">
<style>
  :root {
    --page: #ffffff;
    --frame: #7d7f82;
    --heading: #8a8c8f;
    --ink: #3a3a3c;
    --icon: #555759;
    --white: #ffffff;
  }
  html, body {
    margin: 0;
    padding: 0;
    width: 800px;
    height: 1200px;
    overflow: hidden;
    background: var(--page);
  }
  .canvas {
    display: block;
    width: 800px;
    height: 1200px;
    font-family: "Montserrat", Arial, sans-serif;
  }
  .section-title { fill: var(--heading); font-weight: 800; font-size: 11.5px; letter-spacing: 0.4px; }
  .step-number { fill: var(--white); font-weight: 800; }
  .step-label { fill: var(--white); font-weight: 700; font-size: 8px; }
  .band-label { fill: var(--white); font-weight: 700; font-size: 8.5px; }
  .band-label.end { text-anchor: end; }
  .pillar-number { fill: var(--white); font-weight: 800; font-size: 18px; font-style: italic; }
  .frame { fill: var(--frame); stroke: var(--frame); stroke-linejoin: round; }
  .icon-ring { fill: var(--white); stroke: #c9cacc; stroke-width: 2; }
  .icon-line { fill: none; stroke: var(--icon); stroke-width: 1.6; stroke-linecap: round; stroke-linejoin: round; }
  .icon-white { fill: none; stroke: var(--white); stroke-width: 1.4; stroke-linecap: round; stroke-linejoin: round; }
  .brand-name { fill: var(--ink); font-weight: 500; font-size: 6.5px; letter-spacing: 0.3px; }
  .legacy-title { fill: var(--ink); font-weight: 500; font-size: 14px; }
  .fan-label { fill: var(--white); font-weight: 700; font-size: 8.5px; }
  .divider { stroke: var(--white); stroke-width: 1.6; }
</style>
</head>
<body>
<svg class="canvas" viewBox="0 0 800 1200" xmlns="http://www.w3.org/2000/svg">
  <defs>
    <filter id="soft-shadow" x="-20%" y="-20%" width="140%" height="150%">
      <feDropShadow dx="0" dy="4" stdDeviation="4" flood-color="#000" flood-opacity="0.35"/>
    </filter>
    <linearGradient id="g-discovery" x1="0" y1="0" x2="0" y2="1"><stop offset="0" stop-color="#8cc97a"/><stop offset="1" stop-color="#2fb3c8"/></linearGradient>
    <linearGradient id="g-planning" x1="0" y1="0" x2="1" y2="1"><stop offset="0" stop-color="#7a5cb3"/><stop offset="1" stop-color="#3f3592"/></linearGradient>
    <linearGradient id="g-learning" x1="0" y1="0" x2="1" y2="1"><stop offset="0" stop-color="#f8a11f"/><stop offset="1" stop-color="#e8452a"/></linearGradient>
    <linearGradient id="g-execution" x1="0" y1="0" x2="1" y2="1"><stop offset="0" stop-color="#2db2e6"/><stop offset="1" stop-color="#1f5fae"/></linearGradient>
    <linearGradient id="g-alignment" x1="0" y1="0" x2="1" y2="1"><stop offset="0" stop-color="#f9a51b"/><stop offset="1" stop-color="#ec4f26"/></linearGradient>
    <linearGradient id="g-review" x1="0" y1="0" x2="1" y2="1"><stop offset="0" stop-color="#38b38e"/><stop offset="1" stop-color="#1b7766"/></linearGradient>
    <linearGradient id="g-fan" x1="0" y1="0" x2="1" y2="0.4"><stop offset="0" stop-color="#3fbcc4"/><stop offset="1" stop-color="#2a62b0"/></linearGradient>
    <linearGradient id="g-rule" x1="0" y1="0" x2="1" y2="0"><stop offset="0" stop-color="#2a62b0"/><stop offset="1" stop-color="#3fbcc4"/></linearGradient>
  </defs>

  <!-- ===== Retirement planning process ===== -->
  <g class="process">
    <text class="section-title" x="132" y="45">THE RETIREMENT PLANNING PROCESS</text>
    <g class="frame" stroke-width="30">
      <rect x="137" y="115" width="113" height="85" rx="18"/>
      <rect x="268" y="87" width="162" height="128" rx="22"/>
      <rect x="185" y="190" width="145" height="115" rx="20"/>
      <rect x="348" y="205" width="164" height="128" rx="22"/>
      <rect x="450" y="115" width="138" height="95" rx="20"/>
      <rect x="530" y="205" width="110" height="90" rx="18"/>
      <rect x="250" y="200" width="290" height="110"/>
    </g>

    <g class="step step-planning" filter="url(#soft-shadow)">
      <rect x="268" y="87" width="162" height="128" rx="22" fill="url(#g-planning)"/>
    </g>
    <g class="step step-learning" filter="url(#soft-shadow)">
      <rect x="185" y="190" width="145" height="115" rx="20" fill="url(#g-learning)"/>
    </g>
    <g class="step step-execution" filter="url(#soft-shadow)">
      <rect x="348" y="205" width="164" height="128" rx="22" fill="url(#g-execution)"/>
    </g>
    <g class="step step-review" filter="url(#soft-shadow)">
      <rect x="530" y="205" width="110" height="90" rx="18" fill="url(#g-review)"/>
    </g>
    <g class="step step-discovery" filter="url(#soft-shadow)">
      <rect x="137" y="115" width="113" height="85" rx="18" fill="url(#g-discovery)"/>
      <path d="M198 198 L207 211 L214 198 Z" fill="#2fb3c8"/>
    </g>
    <g class="step step-alignment" filter="url(#soft-shadow)">
      <rect x="450" y="115" width="138" height="95" rx="20" fill="url(#g-alignment)"/>
      <path d="M535 208 L546 222 L553 208 Z" fill="#ee5726"/>
    </g>

    <!-- labels -->
    <text class="step-number" x="203" y="164" font-size="22">01</text>
    <text class="step-label" x="231" y="179" text-anchor="end">DISCOVERY</text>
    <text class="step-label" x="231" y="190" text-anchor="end">MEETING</text>
    <text class="step-number" x="287" y="142" font-size="24">03</text>
    <text class="step-label" x="287" y="158">PLANNING</text>
    <text class="step-number" x="203" y="256" font-size="24">02</text>
    <text class="step-label" x="203" y="272">LEARNING</text>
    <text class="step-number" x="364" y="276" font-size="24">04</text>
    <text class="step-label" x="364" y="291">EXECUTION</text>
    <text class="step-number" x="464" y="163" font-size="22">05</text>
    <text class="step-label" x="464" y="178">ALIGNMENT</text>
    <text class="step-number" x="545" y="253" font-size="22">06</text>
    <text class="step-label" x="545" y="270">REVIEW</text>

    <!-- icons -->
    <circle class="icon-ring" cx="168" cy="143" r="20"/>
    <g class="icon-line"><circle cx="163" cy="137" r="4"/><circle cx="174" cy="137" r="4"/><path d="M155 152 Q163 141 170 152 M167 152 Q174 141 182 152"/></g>
    <circle class="icon-ring" cx="388" cy="146" r="28"/>
    <g class="icon-line"><path d="M370 162 H406 M374 162 V154 H380 V162 M383 162 V148 H389 V162 M392 162 V142 H398 V162 M372 148 L400 130 M394 130 H400 V136"/></g>
    <circle class="icon-ring" cx="290" cy="247" r="27"/>
    <g class="icon-line"><rect x="277" y="240" width="22" height="20"/><path d="M281 248 L287 256 L304 232" stroke="#e8452a" stroke-width="2.4"/></g>
    <circle class="icon-ring" cx="465" cy="270" r="30"/>
    <g class="icon-line"><path d="M442 264 H462 Q468 264 468 270 Q468 276 462 276 H446 M446 270 H458"/><circle cx="475" cy="270" r="8"/><circle cx="475" cy="270" r="3"/></g>
    <circle class="icon-ring" cx="555" cy="155" r="22"/>
    <g class="icon-line" stroke="#ec4f26"><path d="M544 150 A12 12 0 0 1 566 152 M566 152 L568 145 M566 152 L560 150 M566 160 A12 12 0 0 1 544 158 M544 158 L542 165 M544 158 L550 160"/></g>
    <circle class="icon-ring" cx="603" cy="247" r="22"/>
    <g class="icon-line"><rect x="592" y="236" width="18" height="22"/><path d="M596 243 H606 M596 248 H606 M596 253 H602 M614 236 L603 254"/></g>

    <text class="brand-name" x="528" y="348">Brenton Wealth Management</text>
  </g>

  <!-- ===== Comprehensive investment management ===== -->
  <g class="investment">
    <g class="frame" stroke-width="0">
      <rect x="180" y="430" width="262" height="82" rx="16"/>
      <rect x="396" y="508" width="206" height="252" rx="16"/>
      <rect x="180" y="566" width="200" height="68" rx="14"/>
      <rect x="180" y="642" width="180" height="78" rx="14"/>
      <rect x="292" y="560" width="190" height="210" rx="16"/>
    </g>
    <text class="section-title" x="467" y="442">COMPREHENSIVE</text>
    <text class="section-title" x="467" y="458">INVESTMENT</text>
    <text class="section-title" x="467" y="474">MANAGEMENT</text>

    <!-- bands -->
    <rect x="180" y="452" width="195" height="45" fill="#9fd6ec"/>
    <rect x="410" y="530" width="190" height="46" fill="#8fb3de"/>
    <rect x="180" y="578" width="170" height="45" fill="#9fd9c8"/>
    <rect x="445" y="603" width="155" height="43" fill="#f79a22"/>
    <rect x="180" y="655" width="150" height="45" fill="#f8a52c"/>
    <rect x="470" y="690" width="130" height="45" fill="#b8a2d6"/>

    <text class="band-label" x="237" y="467">UNDERSTANDING</text>
    <text class="band-label" x="237" y="479">YOUR RISK</text>
    <text class="band-label" x="237" y="491">TOLERANCE</text>
    <text class="band-label end" x="550" y="553">INVESTMENT</text>
    <text class="band-label end" x="550" y="565">SELECTION</text>
    <text class="band-label" x="237" y="598">ASSET</text>
    <text class="band-label" x="237" y="610">ALLOCATION</text>
    <text class="band-label end" x="550" y="623">TAX</text>
    <text class="band-label end" x="550" y="635">EFFICIENCY</text>
    <text class="band-label" x="237" y="678">DISTRIBUTION</text>
    <text class="band-label" x="237" y="690">STRATEGY</text>
    <text class="band-label" x="497" y="704">BEHAVIOR</text>
    <text class="band-label" x="497" y="716">FINANCE</text>
    <text class="band-label" x="497" y="728">COACHING</text>

    <!-- band icons -->
    <g class="icon-white">
      <path d="M198 472 Q210 458 222 472 Z M210 472 V488 Q210 492 206 490"/>
      <rect x="566" y="537" width="20" height="30"/><path d="M570 545 H582 M570 552 H582 M570 559 H582"/>
      <path d="M198 595 h8 v16 h-8 z M208 592 h8 v19 h-8 z M218 598 h8 v13 h-8 z"/>
      <rect x="566" y="610" width="18" height="30"/><path d="M569 614 H581 V620 H569 Z M569 625 h3 M575 625 h3 M569 631 h3 M575 631 h3"/>
      <circle cx="208" cy="676" r="12"/><path d="M208 664 V676 L219 682 M208 676 L198 684"/>
      <path d="M563 730 L570 714 L577 730 Z"/><circle cx="570" cy="710" r="3"/><path d="M578 712 L583 704 L588 708 L594 698"/>
    </g>

    <!-- pillars: left face, right face, top -->
    <g class="pillar">
      <path d="M370 450 L393 458 L393 735 L370 727 Z" fill="#5bc2ec"/>
      <path d="M393 458 L416 450 L416 727 L393 735 Z" fill="#2f8fd8"/>
      <path d="M370 450 L393 442 L416 450 L393 458 Z" fill="#8ed9f5"/>
      <text class="pillar-number" x="374" y="487">1</text>
    </g>
    <g class="pillar">
      <path d="M392 525 L415 533 L415 740 L392 732 Z" fill="#3a7fd0"/>
      <path d="M415 533 L438 525 L438 732 L415 740 Z" fill="#2560b0"/>
      <path d="M392 525 L415 517 L438 525 L415 533 Z" fill="#6aa6e6"/>
      <text class="pillar-number" x="417" y="567">2</text>
    </g>
    <g class="pillar">
      <path d="M345 572 L367 580 L367 745 L345 737 Z" fill="#7fd6c4"/>
      <path d="M367 580 L389 572 L389 737 L367 745 Z" fill="#49b4a2"/>
      <path d="M345 572 L367 564 L389 572 L367 580 Z" fill="#b2ebdf"/>
      <text class="pillar-number" x="349" y="612">3</text>
    </g>
    <g class="pillar">
      <path d="M413 597 L435 605 L435 745 L413 737 Z" fill="#fbd54c"/>
      <path d="M435 605 L457 597 L457 737 L435 745 Z" fill="#f08a24"/>
      <path d="M413 597 L435 589 L457 597 L435 605 Z" fill="#fde07a"/>
      <path d="M413 665 L435 673 L435 745 L413 737 Z" fill="#f27a26"/>
      <text class="pillar-number" x="438" y="638">4</text>
    </g>
    <g class="pillar">
      <path d="M323 643 L346 651 L346 750 L323 742 Z" fill="#f9d84a"/>
      <path d="M346 651 L369 643 L369 742 L346 750 Z" fill="#f5a623"/>
      <path d="M323 643 L346 635 L369 643 L346 651 Z" fill="#fde88a"/>
      <text class="pillar-number" x="327" y="697">5</text>
    </g>
    <g class="pillar">
      <path d="M436 682 L458 690 L458 755 L436 747 Z" fill="#c9b3e3"/>
      <path d="M458 690 L480 682 L480 747 L458 755 Z" fill="#8d6bbf"/>
      <path d="M436 682 L458 674 L480 682 L458 690 Z" fill="#e0d2f2"/>
      <text class="pillar-number" x="461" y="724">6</text>
    </g>

    <text class="brand-name" x="188" y="546">Brenton Wealth Management</text>
  </g>

  <!-- ===== Legacy and estate planning ===== -->
  <g class="legacy">
    <path class="frame" stroke-width="2" d="M215 880 Q300 800 420 812 Q595 830 598 1000 Q595 1165 420 1168 Q300 1168 250 1110 Q200 1050 205 960 Q206 910 215 880 Z"/>
    <ellipse cx="390" cy="990" rx="185" ry="165" fill="url(#g-fan)"/>
    <g class="divider">
      <line x1="390" y1="990" x2="432" y2="826"/>
      <line x1="390" y1="990" x2="556" y2="910"/>
      <line x1="390" y1="990" x2="568" y2="1050"/>
      <line x1="390" y1="990" x2="445" y2="1148"/>
    </g>

    <g class="icon-white">
      <path d="M360 867 Q350 882 365 886 Q380 882 370 867 Z M362 867 L368 860"/><path d="M371 876 L381 870 M371 880 L383 884"/>
      <path d="M413 905 L425 898 L437 905 Z M415 908 v12 M422 908 v12 M429 908 v12 M436 908 v12 M411 922 H439"/>
      <rect x="426" y="962" width="26" height="18"/><path d="M434 962 v-4 h10 v4 M426 970 H452"/>
      <rect x="418" y="1034" width="18" height="20"/><path d="M427 1034 V1054 M418 1041 H436 M427 1034 Q420 1024 427 1028 Q434 1024 427 1034"/>
      <rect x="376" y="1074" width="12" height="16"/><path d="M364 1088 L374 1082 L380 1090 L368 1096"/>
    </g>

    <text class="fan-label" x="318" y="860">BENEFICIARIES</text>
    <text class="fan-label" x="452" y="915">TRUSTS</text>
    <text class="fan-label" x="470" y="965">ESTATE</text>
    <text class="fan-label" x="470" y="977">TAXES AND</text>
    <text class="fan-label" x="470" y="989">ASSESSMENT</text>
    <text class="fan-label" x="478" y="1048">ANNUAL</text>
    <text class="fan-label" x="478" y="1060">GIVING</text>
    <text class="fan-label" x="333" y="1112">DONATIONS</text>
    <text class="fan-label" x="330" y="1124">AND CHARITY</text>

    <path filter="url(#soft-shadow)" fill="#ffffff" d="M222 935 C228 898 270 888 330 890 C382 893 405 935 408 990 C405 1040 380 1068 330 1076 C275 1084 228 1078 222 1040 Z"/>
    <text class="legacy-title" x="228" y="953">LEGACY AND</text>
    <text class="legacy-title" x="228" y="972">ESTATE PLANNING</text>
    <rect x="228" y="982" width="138" height="3" fill="url(#g-rule)"/>
    <text class="brand-name" x="246" y="1058">Brenton Wealth Management</text>
  </g>
</svg>
</body>
</html>
```